Modern Design Business Card industrial maintenance company

Business card design for Company named Brookvale Equipment Services

Target Market(s)

Industrial

Industry/Entity Type

Maintenance and repair

Contact Information for Business Card

Place holder for address, office phone, mobile number and email

Requirements
Must have
• Clean modern look
Nice to have
• N/a

```html
<!DOCTYPE html>
<html lang="en">
<head>
<meta charset="utf-8">
<title>Brookvale Equipment Services – Business Cards</title>
<link href="https://fonts.googleapis.com/css2?family=Figtree:wght@400;600&display=swap" rel="stylesheet">
<style>
  :root{
    --stage:#333333;
    --ink:#111111;
    --paper:#ffffff;
    --card-dark:#050505;
    --gear-tone:#1a1a1a;
    --light:#ffffff;
  }
  *{margin:0;padding:0;box-sizing:border-box}
  html,body{width:1200px;height:1200px;overflow:hidden;background:var(--stage)}
  body{position:relative;font-family:"Figtree",Arial,sans-serif;color:var(--ink)}
  .card{position:absolute;box-shadow:0 10px 30px rgba(0,0,0,.45);overflow:hidden}
  .card--front{left:199px;top:99px;width:543px;height:310px;background:var(--card-dark)}
  .card--contact{left:206px;top:453px;width:530px;height:303px;background:var(--paper)}
  .card--personal{left:207px;top:800px;width:527px;height:301px;background:var(--paper)}

  .gear-field{position:absolute;inset:0;
    background:radial-gradient(circle at 40% 40%,var(--gear-tone) 0,var(--card-dark) 70%)}

  .lockup{position:absolute;display:flex;align-items:center;gap:10px}
  .lockup__ring{border-radius:50%;flex:none}
  .lockup__name{font-weight:600;letter-spacing:.04em;text-transform:uppercase;line-height:1.15}

  .front-lockup{right:48px;top:150px;flex-direction:column;align-items:flex-end;gap:12px}
  .front-lockup .lockup__ring{width:68px;height:68px;border:3px solid var(--light);margin-right:55px}
  .front-lockup .lockup__name{color:var(--light);font-size:17px;text-align:right}

  .contact-lockup{left:25px;top:74px;gap:18px}
  .contact-lockup .lockup__ring{width:86px;height:86px;border:5px solid var(--ink)}
  .contact-lockup .lockup__name{font-size:24px;color:var(--ink)}

  .contacts{position:absolute;list-style:none;font-size:14.5px;font-weight:600;line-height:1.3}
  .contacts li{display:flex;gap:8px;align-items:flex-start;margin-bottom:5px}
  .contacts svg{width:17px;height:17px;flex:none;margin-top:1px}
  .card--contact .contacts{left:40px;top:193px}
  .card--personal .contacts{left:40px;top:202px}

  .personal-lockup{left:30px;top:66px}
  .personal-lockup .lockup__name{font-size:17px;color:var(--ink)}
  .person{position:absolute;left:38px;top:136px}
  .person__name{font-size:22px;font-weight:600}
  .person__role{font-size:15px;font-weight:400}
  .big-ring{position:absolute;left:330px;top:86px;width:166px;height:166px;border-radius:50%;border:9px solid var(--ink)}

  .side-lockup{position:absolute;left:950px;top:346px;width:130px;height:550px}
  .side-lockup .lockup__ring{position:absolute;left:0;top:0;width:126px;height:126px;border:5px solid var(--light)}
  .side-lockup .lockup__name{position:absolute;left:63px;top:160px;transform-origin:0 0;transform:rotate(90deg) translateY(-50%);
    white-space:nowrap;color:var(--light);font-size:31px}
</style>
</head>
<body>
  <section class="card card--front" aria-label="Card front">
    <div class="gear-field" role="img" aria-label="Dark pattern of interlocking machine gears"></div>
    <div class="lockup front-lockup">
      <span class="lockup__ring"></span>
      <span class="lockup__name">Brookvale Equipment Services</span>
    </div>
  </section>

  <section class="card card--contact" aria-label="Company contact card">
    <div class="lockup contact-lockup">
      <span class="lockup__ring"></span>
      <span class="lockup__name">Brookvale<br>Equipment Services</span>
    </div>
    <ul class="contacts">
      <li><svg viewBox="0 0 20 20"><rect x="1" y="4" width="18" height="12" fill="none" stroke="#111" stroke-width="2"/><path d="M1 4l9 7 9-7" fill="none" stroke="#111" stroke-width="2"/></svg><span style="font-weight:400">info@brookvaleequip.com</span></li>
      <li><svg viewBox="0 0 20 20"><path d="M4 2l4 1 1 4-2 2c1 2 3 4 5 5l2-2 4 1 1 4-2 2C9 19 1 11 2 4z" fill="#111"/></svg><span>0900 555 0142</span></li>
      <li><svg viewBox="0 0 20 20"><path d="M10 1a6 6 0 0 0-6 6c0 5 6 11 6 11s6-6 6-11a6 6 0 0 0-6-6z" fill="#111"/><circle cx="10" cy="7" r="2.2" fill="#fff"/></svg><span>48 Harbor Row #2, Fairview,<br>Alaska 99510, USA</span></li>
    </ul>
  </section>

  <section class="card card--personal" aria-label="Personal card">
    <div class="lockup personal-lockup">
      <span class="lockup__name">Brookvale Equipment Services</span>
    </div>
    <div class="person">
      <p class="person__name">Daniel Reyes</p>
      <p class="person__role">Director</p>
    </div>
    <ul class="contacts">
      <li><svg viewBox="0 0 20 20"><rect x="1" y="4" width="18" height="12" fill="none" stroke="#111" stroke-width="2"/><path d="M1 4l9 7 9-7" fill="none" stroke="#111" stroke-width="2"/></svg><span style="font-weight:400">info@brookvaleequip.com</span></li>
      <li><svg viewBox="0 0 20 20"><path d="M4 2l4 1 1 4-2 2c1 2 3 4 5 5l2-2 4 1 1 4-2 2C9 19 1 11 2 4z" fill="#111"/></svg><span>0900 555 0142</span></li>
      <li><svg viewBox="0 0 20 20"><path d="M10 1a6 6 0 0 0-6 6c0 5 6 11 6 11s6-6 6-11a6 6 0 0 0-6-6z" fill="#111"/><circle cx="10" cy="7" r="2.2" fill="#fff"/></svg><span>48 Harbor Row #2, Fairview,<br>Alaska 99510, USA</span></li>
    </ul>
    <span class="big-ring"></span>
  </section>

  <div class="side-lockup" aria-label="Vertical brand lockup">
    <span class="lockup__ring"></span>
    <span class="lockup__name">Brookvale Equipment Services</span>
  </div>
</body>
</html>
```